Waterproofing Adhesive company needs design for bucket

We need a design for our 20kg/15kg and 4 kg bucket, Our companys name is Zorvane Co LLC based in Umm Al Quwain, United Arab Emirates . Our main business is into waterproofing paint and Adhesive manufacturing. We are looking for a creative design for our buckets and paper bags. The design have to be attractive, The color theme of our company is light orange and yellow. I have attached the company logo along with this.

Target Market(s)

B2b , construction companys
Maintenance company

Industry/Entity Type

Manufacturer

Requirements
Must have
• It must have the company logo
• a spcae in centre to write the different products names
Nice to have
• A attractive design for placing the bucket in retail shops

```html
<!DOCTYPE html>
<html lang="en">
<head>
<meta charset="utf-8">
<title>Zorvane Co LLC – Hydrelle Waterproofing Paint</title>
<link href="https://fonts.googleapis.com/css2?family=Anton&family=Oswald:wght@500;700&display=swap" rel="stylesheet">
<style>
  :root {
    --bg: #e9e9e9;
    --label-top: #fbf9f6;
    --label-bottom: #f4efe6;
    --orange: #e8a02a;
    --orange-deep: #e2670a;
    --gold: #f0c24a;
    --cream: #f6e3b0;
    --shadow: rgba(60, 40, 10, 0.35);
  }
  * { margin: 0; padding: 0; box-sizing: border-box; }
  html, body { width: 1200px; height: 1026px; overflow: hidden; }
  body {
    background: var(--bg);
    position: relative;
    font-family: "Oswald", sans-serif;
  }
  .label {
    position: absolute;
    left: 160px; top: 150px;
    width: 880px; height: 820px;
    background: linear-gradient(180deg, var(--label-top), var(--label-bottom));
    overflow: hidden;
  }
  .brand {
    position: absolute;
    left: 80px; top: 190px;
    display: flex; align-items: center; gap: 12px;
  }
  .brand-mark {
    width: 34px; height: 34px; border-radius: 50%;
    background: var(--orange-deep);
  }
  .brand-name {
    font-family: "Oswald", sans-serif;
    font-weight: 500;
    font-size: 30px;
    color: var(--orange-deep);
    white-space: nowrap;
  }
  .product {
    position: absolute;
    left: 300px; top: 135px;
    width: 480px;
    text-align: right;
    color: var(--orange);
    font-family: "Anton", sans-serif;
    text-shadow: 2px 3px 3px var(--shadow);
  }
  .product-name {
    display: flex; justify-content: flex-end; align-items: flex-end; gap: 8px;
    font-size: 92px; line-height: 1; letter-spacing: 1px;
    text-transform: uppercase; font-weight: 400;
  }
  .product-rule {
    height: 4px; background: var(--orange); margin: 10px 0 6px;
    box-shadow: 1px 2px 2px var(--shadow);
  }
  .product-type {
    font-size: 62px; line-height: 1.02; text-transform: uppercase;
  }
  .wave-art { position: absolute; left: 0; top: 330px; width: 880px; height: 490px; }
  .guarantee {
    position: absolute;
    left: 480px; top: 575px;
    width: 340px; height: 165px;
    background: rgba(150, 110, 60, 0.28);
  }
  .guarantee-band {
    position: absolute; left: 118px; top: 52px; width: 222px; height: 113px;
    background: rgba(240, 150, 70, 0.55);
  }
  .guarantee-number {
    position: absolute; left: 18px; top: 8px;
    font-family: "Anton", sans-serif;
    font-size: 150px; line-height: 1;
    color: var(--orange-deep);
    text-shadow: 3px 4px 4px rgba(0,0,0,0.45);
  }
  .guarantee-title {
    position: absolute; left: 112px; top: 6px;
    font-family: "Anton", sans-serif;
    font-size: 32px; line-height: 1.2;
    color: var(--gold);
    text-transform: uppercase; letter-spacing: 0.5px;
    white-space: nowrap;
    text-shadow: 1px 2px 2px rgba(0,0,0,0.35);
  }
  .guarantee-text {
    position: absolute; left: 126px; top: 60px;
    font-family: "Oswald", sans-serif; font-weight: 500;
    font-size: 16px; line-height: 1.25; color: #fff;
    text-transform: uppercase;
    white-space: nowrap;
    text-shadow: 1px 1px 2px rgba(0,0,0,0.4);
  }
</style>
</head>
<body>
  <main class="label">
    <svg class="wave-art" viewBox="0 0 880 490" role="img" aria-label="Flowing translucent orange and yellow silk wave decoration">
      <defs>
        <linearGradient id="waveFill" x1="0" y1="0" x2="1" y2="1">
          <stop offset="0" stop-color="#f7dd9a" stop-opacity="0.7"/>
          <stop offset="0.55" stop-color="#f0b443" stop-opacity="0.75"/>
          <stop offset="1" stop-color="#e89a20" stop-opacity="0.85"/>
        </linearGradient>
      </defs>
      <path d="M0 120 C120 20 260 60 340 240 C400 380 470 420 560 330 C640 250 760 220 880 40 L880 490 L0 490 Z" fill="url(#waveFill)"/>
    </svg>

    <div class="brand">
      <span class="brand-mark"></span>
      <span class="brand-name">Zorvane Co LLC</span>
    </div>

    <section class="product">
      <h1 class="product-name">Hydrelle
        <svg width="58" height="98" viewBox="0 0 58 98" aria-hidden="true">
          <path d="M29 2 C40 30 56 48 56 68 A27 27 0 0 1 2 68 C2 48 18 30 29 2 Z" fill="#f2b13a" stroke="#d98a10" stroke-width="3"/>
        </svg>
      </h1>
      <div class="product-rule"></div>
      <p class="product-type">Waterproofing<br>Paint</p>
    </section>

    <aside class="guarantee">
      <div class="guarantee-band"></div>
      <span class="guarantee-number">5</span>
      <span class="guarantee-title">Year Guarantee</span>
      <p class="guarantee-text">Water-proof and mold &amp;<br>mildew-proof paint film</p>
    </aside>
  </main>
</body>
</html>
```